My name is Delia Forsythe,I want to create a web page for my personal dog grooming business. The name on the web page can be "Delia's Dog Grooming" I am located in Brookhaven Kansas. The page would help grow my customer base. Before and after pictures would display the quality of work that I do. On my page I can provide information about myself, my services, and pricing.
Updates

I have updated project to guaranteed pay

Please try to incorporate a schnauzer in an icon or logo. My dog is a schnauzer. THANKS!!!!!!!!!!!!

Target Market(s)

Dog Owners

Industry/Entity Type

Business

Requirements
Must have
• -A spot for before and after pictures.
-An about me section
-A section to make an appointment
Nice to have
• My favorite Color is purple. I think different shades of purple would be nice or purple with a light green

please incorporate a schnauzer in any icon or logo. My dog is a schnauzer.

```html
<!DOCTYPE html>
<html lang="en">
<head>
<meta charset="utf-8">
<title>Delia's Dog Grooming</title>
<link href="https://fonts.googleapis.com/css2?family=Didact+Gothic&family=Arimo:wght@400;700&display=swap" rel="stylesheet">
<style>
:root{
  --purple:#5d1156;
  --purple-panel:#6d2266;
  --lime:#6cc20e;
  --lime-dark:#4f9a08;
  --lime-light:#8edb2c;
  --white:#ffffff;
  --ink:#111111;
  --field:#ffffff;
}
*{box-sizing:border-box;margin:0;padding:0}
html,body{width:1027px;height:1200px;overflow:hidden}
body{background:var(--purple);font-family:'Arimo',Arial,sans-serif;color:var(--white);position:relative}
.abs{position:absolute}
.site-header{left:0;top:0;width:1027px;height:104px;background:linear-gradient(180deg,var(--lime-light),var(--lime))}
.site-title{left:50px;top:24px;font-family:'Arimo',Arial,sans-serif;font-weight:400;font-size:48px;color:var(--purple);white-space:nowrap}
.hero{left:630px;top:40px;width:340px;height:250px;border-radius:50%;background:radial-gradient(ellipse at center,#d75fd0 0%,#a02a98 35%,rgba(93,17,86,0) 70%)}
.hero-photo{left:660px;top:55px;width:300px;height:225px;border-radius:40% 40% 30% 30%;background:radial-gradient(ellipse at 50% 55%,#d8d8d8 0%,#9a9a9a 45%,rgba(120,120,120,0) 72%)}
.heading{font-family:'Didact Gothic',sans-serif;font-size:32px;color:var(--white);font-weight:400}
.panel{background:var(--purple-panel);border-radius:10px}
.about-text{left:29px;top:170px;width:635px;height:254px;padding:12px 14px;font-size:14.8px;line-height:26.6px;text-align:justify}
.connect{left:757px;top:337px;width:210px;text-align:center;font-size:11.5px;font-weight:700}
.social{left:757px;top:360px;width:210px;height:56px;border-radius:28px;display:flex;align-items:center;justify-content:space-around;padding:0 10px}
.social span{display:flex;align-items:center;gap:3px;font-size:10.5px}
.social i{display:block;width:12px;height:12px;border-radius:50%;background:var(--lime)}
.gallery{left:29px;top:485px;width:674px;height:282px}
.tab{width:86px;height:32px;background:linear-gradient(var(--lime-light),var(--lime-dark));border-radius:4px 4px 0 0;text-align:center;line-height:32px;font-size:15px;font-weight:700}
.frame{width:207px;height:280px;background:var(--lime);border:3px solid var(--lime-light);padding:12px 11px}
.frame div{width:100%;height:100%;background:linear-gradient(160deg,#d9d3c8 0%,#8e8a85 55%,#3a3634 100%)}
.arrow{width:38px;height:38px;border-radius:8px;background:linear-gradient(var(--lime-light),var(--lime-dark))}
.services-text{left:720px;top:485px;width:283px;height:282px;padding:11px 17px;font-size:14.4px;line-height:22.6px;text-align:justify}
.more{font-size:13.3px;display:flex;align-items:center;gap:4px;justify-content:flex-end}
.more b{display:inline-block;width:11px;height:11px;border-radius:50%;background:var(--lime);color:var(--white);font-size:11px;line-height:11px;text-align:center}
.appt{left:29px;top:858px;width:635px;height:245px}
.label{font-family:'Didact Gothic',sans-serif;font-size:21px}
.field{background:var(--field);height:29px;color:#aaa;font-family:Georgia,serif;font-size:12px;padding:0 9px;line-height:29px}
.select-btn{width:29px;height:29px;background:#cfcfcf;color:#233;font-size:16px;text-align:center;line-height:29px}
.submit{width:102px;height:27px;border-radius:4px;background:linear-gradient(var(--lime-light),var(--lime-dark));font-size:14px;line-height:27px;padding-left:24px}
.prices{left:720px;top:858px;width:283px;height:245px;padding:6px 12px}
.sale{font-size:22px;font-weight:400;font-family:'Didact Gothic',sans-serif;border-bottom:1px solid #9b5a94;padding-bottom:2px;display:inline-block}
.sale em{font-style:normal;color:var(--lime)}
.pup{position:absolute;left:12px;width:56px;height:55px;background:linear-gradient(135deg,#6f6a5e,#2f2d2a)}
.pup-info{position:absolute;left:77px;font-size:13.3px;line-height:19px}
.pup-info u{text-decoration:none;border-bottom:1px solid var(--white)}
.site-footer{left:0;top:1120px;width:1027px;height:80px;background:var(--lime)}
.copy{left:16px;top:1180px;font-size:12.5px;color:var(--ink)}
.contact{right:18px;top:1131px;text-align:right;font-size:12.5px;line-height:15px;font-style:normal}
.contact strong{display:block;color:var(--ink);margin-bottom:7px}
</style>
</head>
<body>
<header class="abs site-header"></header>
<h1 class="abs site-title">Delia's Dog Grooming</h1>
<div class="abs hero"></div>
<div class="abs hero-photo" role="img" aria-label="Two schnauzers lying side by side"></div>

<h2 class="abs heading" style="left:30px;top:120px">About Me</h2>
<p class="abs panel about-text">Hi, my name is Delia Forsythe and my love for animals started as a young child; My dog is a schnauzer. however, it didn't end there. I started out working and caring for animals in the kennels; from there I started to work with animals in rescue. From seeing them in the conditions they were in and just how scared and fragile they were I wanted to do something more.&nbsp; Apprenticing taught me the standard cuts and grooms of all breeds of dogs. To me grooming is never just a job; each dog and cat like in rescue, is an individual. Each animal has different needs and must be treated according to them. I am also a current volunteer with Brookhaven Kansas ; however, I love all&nbsp; sizes of schnauzer dogs.</p>

<p class="abs connect">CONNECT WITH ME</p>
<nav class="abs panel social">
  <span><i></i>Chirp</span><span><i></i>Pals</span><span><i></i>Snaps</span><span><i></i>Feed</span>
</nav>

<section class="abs panel gallery"></section>
<div class="abs tab" style="left:160px;top:459px">Before</div>
<div class="abs tab" style="left:441px;top:459px">After</div>
<div class="abs frame" style="left:95px;top:487px"><div role="img" aria-label="Schnauzer on grooming table before grooming"></div></div>
<div class="abs frame" style="left:377px;top:487px"><div role="img" aria-label="Schnauzer on grooming table after grooming"></div></div>
<div class="abs arrow" style="left:45px;top:608px"><svg width="38" height="38" viewBox="0 0 38 38"><path d="M23 11 L13 19 L23 27 Z" fill="#234a04"/></svg></div>
<div class="abs arrow" style="left:613px;top:608px"><svg width="38" height="38" viewBox="0 0 38 38"><path d="M15 11 L25 19 L15 27 Z" fill="#234a04"/></svg></div>

<h2 class="abs heading" style="left:720px;top:427px">Services</h2>
<div class="abs panel services-text">
  <p>Service dogs are trained to assist disabled individuals, so they may lead more independent lives. The work they do to serve people with disabili-ties, is truly remarkable.</p>
  <p style="margin-top:22px">These working dogs actually become an extension of their owners. They bring into their owner's lives a sense of security, freedom, independence, as well as companionship.</p>
  <p class="more"><b>+</b>More Info</p>
</div>

<h2 class="abs heading" style="left:30px;top:800px">Appointment</h2>
<form class="abs panel appt">
  <span class="abs label" style="left:17px;top:22px">Name&nbsp;&nbsp;&nbsp;:</span>
  <div class="abs field" style="left:103px;top:25px;width:194px">Enter Your Name</div>
  <span class="abs label" style="left:17px;top:63px">State *&nbsp;&nbsp;:</span>
  <div class="abs field" style="left:103px;top:66px;width:194px"></div>
  <span class="abs label" style="left:17px;top:105px">Country :</span>
  <div class="abs field" style="left:103px;top:108px;width:194px"></div>
  <span class="abs label" style="left:17px;top:147px">Date *&nbsp;&nbsp;&nbsp;:</span>
  <div class="abs field" style="left:103px;top:150px;width:165px">Select Date</div>
  <div class="abs select-btn" style="left:268px;top:150px">▼</div>
  <span class="abs label" style="left:17px;top:189px">Time *&nbsp;&nbsp;&nbsp;:</span>
  <div class="abs field" style="left:103px;top:194px;width:165px">Select Time</div>
  <div class="abs select-btn" style="left:268px;top:194px">▼</div>
  <span class="abs label" style="left:334px;top:22px">Email ID :</span>
  <div class="abs field" style="left:424px;top:25px;width:194px">Enter Your E-mail ID</div>
  <span class="abs label" style="left:334px;top:63px">Phone&nbsp;&nbsp;&nbsp;&nbsp;:</span>
  <div class="abs field" style="left:424px;top:68px;width:194px"></div>
  <span class="abs label" style="left:334px;top:109px">Notes/Comments :</span>
  <div class="abs field" style="left:334px;top:147px;width:284px;height:46px;border-radius:4px"></div>
  <div class="abs submit" style="left:516px;top:207px">Submit&nbsp;&nbsp;▹</div>
</form>

<h2 class="abs heading" style="left:720px;top:800px">Prices</h2>
<div class="abs panel prices">
  <h3 class="sale">Puppies for <em>Sale</em></h3>
  <div class="pup" style="top:55px" role="img" aria-label="Miniature schnauzer puppy Chandler"></div>
  <div class="pup-info" style="top:36px"><u>Chandler</u><br>Breed: Miniature Schnauzer<br>Sex: Male<br>Age: 4 Weeks<br>Price: $900 USD</div>
  <p class="more abs" style="right:10px;top:111px"><b>+</b>More Info</p>
  <div class="pup" style="top:162px" role="img" aria-label="Miniature schnauzer puppy, pending sale"></div>
  <div class="pup-info" style="top:143px"><u>Pending</u><br>Breed: Miniature Schnauzer<br>Sex: Male<br>Age: 8 Weeks<br>Price: $600 USD</div>
  <p class="more abs" style="right:10px;top:218px"><b>+</b>More Info</p>
</div>

<footer class="abs site-footer"></footer>
<p class="abs copy">©2012 <b>delia's dog grooming</b>. All rights reserved</p>
<address class="abs contact"><strong>Contact Me</strong>Delia Forsythe<br>Brookhaven<br>Kansas</address>
</body>
</html>
```